Beauty Therapy Web Design

I need a web page design for a small beauty therapy clinic, the owner is currently the only beauty therapist working there.
We require the following pages:
Home
About
Treatments
Nails
Courses
Contact
I will attach the clinics business card, treatment menu and signage so that you get a feeling for the branding colours etc.
This is the first website for the beauty therapist, she would like to attract new clients and also tourists that come in on the cruise ships. The thing that sets her apart from other clinics is that she welcomes texting for appointments.
I have selected refundable because I have never done this before so I don't know what to expect, I have the full intention of going through with it as long as I get a good design.
Feel free to ask for further information
Reason: Project extended as I am away for work and am unable to meet with the owner.
Target Market(s)
Females 18 to 50
Industry/Entity Type
Business
Look and feel
Each slider illustrates characteristics of the customer's brand and the style your logo design should communicate.

```html
<!DOCTYPE html>
<html lang="en">
<head>
<meta charset="utf-8">
<title>Lumora Beauty Therapy</title>
<link rel="stylesheet" href="https://fonts.googleapis.com/css2?family=PT+Sans:wght@400;700&display=swap">
<style>
:root{
  --gold-light:#f3d27a;
  --gold:#e2ae2c;
  --gold-dark:#b8860b;
  --orange:#f2a41e;
  --purple-deep:#3a1a5c;
  --purple:#4a2574;
  --purple-mid:#5a3289;
  --purple-line:#6d4a9a;
  --ink:#3a3a3a;
  --white:#ffffff;
  --footer:#3b1a5e;
}
*{margin:0;padding:0;box-sizing:border-box}
html,body{width:1200px;height:956px;overflow:hidden}
body{
  position:relative;
  font-family:"PT Sans",sans-serif;
  background:linear-gradient(180deg,var(--purple-deep) 300px,var(--purple) 600px,var(--purple-mid) 900px);
  color:var(--white);
}
.hero-bg{position:absolute;left:0;top:0;width:1200px;height:440px}
.main-nav{
  position:absolute;left:0;top:0;width:1200px;height:33px;
  background:linear-gradient(180deg,var(--gold-light),var(--gold) 60%,var(--gold-dark));
  display:flex;align-items:center;font-weight:700;font-size:13px;letter-spacing:.5px;color:#3a2a10;
}
.main-nav a{position:absolute;top:0;height:33px;line-height:33px;color:inherit;text-decoration:none}
.main-nav .current{left:117px;width:72px;text-align:center;background:var(--purple);color:var(--white)}
.main-nav .sep{position:absolute;top:0;line-height:33px;color:#3a2a10}
.brand{position:absolute;left:146px;top:48px;color:var(--purple);font-size:52px;font-weight:400;line-height:1}
.brand small{display:block;font-size:24px;margin-left:96px;margin-top:2px}
.service-panel{position:absolute;left:128px;top:158px;width:292px;height:240px}
.service-list{position:absolute;left:146px;top:168px;list-style:none}
.service-list li{display:flex;align-items:center;height:34px;font-size:16px;color:var(--ink)}
.service-list li::before{content:"";width:22px;height:17px;margin-right:9px;background:linear-gradient(180deg,var(--gold-light),var(--gold-dark))}
.more-btn{
  position:absolute;left:205px;top:372px;width:140px;height:40px;border:2px solid var(--white);border-radius:8px;
  background:linear-gradient(180deg,var(--gold-light),var(--gold-dark));color:var(--white);
  font-size:22px;text-align:center;line-height:36px;
}
.offer-badge{
  position:absolute;left:522px;top:296px;width:126px;height:126px;border-radius:50%;
  background:radial-gradient(circle at 40% 35%,#d6a820,#9a7408);text-align:center;color:var(--white);
}
.offer-badge .big{display:block;font-size:40px;font-weight:700;line-height:1;margin-top:22px}
.offer-badge .off{display:block;font-size:22px;font-weight:700;line-height:.9}
.offer-badge .note{display:block;font-size:11px;line-height:14px;margin-top:4px}
.intro-photo{position:absolute;left:132px;top:444px;width:296px;height:169px;background:var(--white);padding:6px}
.intro-photo div{width:100%;height:100%;background:linear-gradient(135deg,#e9d4c3,#c59a7f 55%,#f2ece8)}
.intro{position:absolute;left:438px;top:446px;width:632px}
.intro h1{font-size:25px;font-weight:400;color:var(--orange);margin-bottom:12px;letter-spacing:.2px}
.intro p{font-size:13.5px;line-height:18px;text-align:justify;margin-left:2px;margin-bottom:18px}
.feature-box{position:absolute;left:120px;top:663px;width:632px;height:220px;border:2px solid var(--purple-line);border-radius:12px}
.feature{position:absolute;top:12px;width:198px;height:196px;font-size:12px;line-height:14.5px}
.feature.active{background:#5c3591}
.feature .pic{margin:3px 4px 0;height:139px}
.feature p{padding:9px 8px 0 8px}
.newsletter{position:absolute;left:782px;top:663px;width:293px;height:220px;border:2px solid var(--purple-line);border-radius:12px}
.newsletter h2{font-size:20px;font-weight:400;margin:10px 0 0 13px}
.newsletter h2 b{color:var(--orange);font-weight:700}
.field{position:absolute;left:22px;font-size:13.5px}
.field span{display:inline-block;width:68px}
.field i{position:absolute;left:68px;top:-5px;width:174px;height:25px;background:linear-gradient(180deg,#cfcfcf,#f6f6f6);border:1px solid #fff}
.join-btn{position:absolute;left:60px;top:164px;width:160px;height:30px;border:1px solid #ddd;background:linear-gradient(180deg,#f4f4f4,#bdbdbd);color:#333;font-weight:700;font-size:13.5px;text-align:center;line-height:28px}
.site-footer{position:absolute;left:0;top:897px;width:1200px;height:59px;background:var(--footer)}
.footer-nav{position:absolute;left:128px;top:11px;font-size:13px}
.footer-nav span{margin:0 6px}
.copyright{position:absolute;left:127px;top:34px;font-size:12.5px}
.social{position:absolute;left:916px;top:19px;display:flex;align-items:center;font-size:14px}
.social i{display:inline-block;width:24px;height:24px;margin-left:12px;border-radius:3px}
</style>
</head>
<body>

<svg class="hero-bg" viewBox="0 0 1200 440" aria-hidden="true">
  <defs>
    <linearGradient id="heroSky" x1="0" y1="0" x2="0" y2="1">
      <stop offset="0" stop-color="#ffffff"/>
      <stop offset="1" stop-color="#eee8ee"/>
    </linearGradient>
    <linearGradient id="portrait" x1="0" y1="0" x2="1" y2="1">
      <stop offset="0" stop-color="#f3ddd0"/>
      <stop offset=".5" stop-color="#c9987d"/>
      <stop offset="1" stop-color="#3a2420"/>
    </linearGradient>
  </defs>
  <path d="M0 33H1200V300C1100 330 950 420 750 410C650 404 580 350 500 330C350 300 150 300 0 330Z" fill="url(#heroSky)"/>
  <path d="M520 33H1200V300C1100 330 960 420 760 412C670 408 600 370 560 335C620 250 560 120 520 33Z" fill="url(#portrait)" role="img" aria-label="Portrait of a woman with long dark hair resting on her hand"/>
</svg>

<nav class="main-nav">
  <a class="current" href="#">HOME</a>
  <span class="sep" style="left:210px">|</span><a href="#" style="left:251px">ABOUT</a>
  <span class="sep" style="left:335px">|</span><a href="#" style="left:371px">TREATMENTS</a>
  <span class="sep" style="left:494px">|</span><a href="#" style="left:535px">NAILS</a>
  <span class="sep" style="left:612px">|</span><a href="#" style="left:649px">COURSES</a>
  <span class="sep" style="left:747px">|</span><a href="#" style="left:784px">CONTACT</a>
</nav>

<div class="brand">Lumora<small>Beauty Therapy.</small></div>

<svg class="service-panel" viewBox="0 0 292 240" aria-hidden="true">
  <defs>
    <linearGradient id="panelFill" x1="0" y1="0" x2="0" y2="1">
      <stop offset="0" stop-color="#ffffff"/>
      <stop offset="1" stop-color="#d9d9d9"/>
    </linearGradient>
  </defs>
  <path d="M14 1H278Q291 1 291 14V205Q220 240 146 240Q70 240 1 205V14Q1 1 14 1Z" fill="url(#panelFill)" stroke="#ffffff" stroke-width="2"/>
</svg>
<ul class="service-list">
  <li>Facials</li>
  <li>Waxing</li>
  <li>Acrylic &amp; Gel Nails</li>
  <li>Eye lash Brow tints</li>
  <li>Manicures / Pedicures</li>
  <li>spray tans</li>
</ul>
<div class="more-btn">More Info.</div>

<div class="offer-badge">
  <span class="big">25%</span><span class="off">OFF</span>
  <span class="note">Perfection in<br>Hair Beauty &amp; Look</span>
</div>

<div class="intro-photo"><div role="img" aria-label="Woman receiving a relaxing head massage"></div></div>
<section class="intro">
  <h1>Lorem Ipsum is the printing and typesetting industry.</h1>
  <p>It was popularised in the 1960s with the release of Typeset sheets containing Lorem Ipsum passages, and more recently with desktop publishing the release of Typeset sheets containing Lorem Ipsum passages, and more recently with desktop</p>
  <p>Publishing the release of Typeset sheets containing Lorem Ipsum passages, and more recently with desktop publishing software like Folio Layout including versions of Lorem Ipsum.It was popularised in the 1960s with the release.</p>
</section>

<section class="feature-box">
  <div class="feature active" style="left:6px">
    <div class="pic" role="img" aria-label="Woman enjoying a facial massage with lilies" style="background:linear-gradient(135deg,#f4ece6,#d4ab93 60%,#f1dfe6)"></div>
    <p>It was popularised in the 1960s with sheets containing Lorem Ipsum passages,</p>
  </div>
  <div class="feature" style="left:213px">
    <div class="pic" role="img" aria-label="Fingernails being shaped with a nail file" style="background:linear-gradient(135deg,#f6e6dc,#e0b9a4 55%,#c9c4c2)"></div>
    <p>It was popularised in the 1960s with sheets containing Lorem Ipsum passages,</p>
  </div>
  <div class="feature" style="left:420px">
    <div class="pic" role="img" aria-label="Nail polish being applied during a manicure" style="background:linear-gradient(135deg,#e9b7a7,#f0c9bd 50%,#d7a0b4)"></div>
    <p style="text-align:justify">It was popularised in the 1960s with sheets containing Lorem Ipsum passages,</p>
  </div>
</section>

<section class="newsletter">
  <h2>Sign up for <b>our Newsletters</b></h2>
  <div class="field" style="top:50px"><span>Name:</span><i></i></div>
  <div class="field" style="top:86px"><span>Surname:</span><i></i></div>
  <div class="field" style="top:121px"><span>Email:</span><i></i></div>
  <div class="join-btn">Join the mailing list</div>
</section>

<footer class="site-footer">
  <div class="footer-nav">Home<span>|</span>About <span>|</span>Treatments<span>|</span>Nails<span>|</span>Courses<span>|</span>Contact</div>
  <div class="copyright">© 2012 Lumora Beauty Therapy , Inc. All rights reserved.</div>
  <div class="social">Connect us:
    <i style="background:#3b5998" aria-label="Social profile"></i>
    <i style="background:#2fa8dc" aria-label="Social profile"></i>
    <i style="background:#1d7fb0" aria-label="Social profile"></i>
  </div>
</footer>

</body>
</html>
```